KV Group

We need a new website for our company and since we had a very good work done for our logo in this site, we're back for the entire job.

Our company name is Marlowe Capital Group. We're adding files of examples of what we have done today. In my opinion we need a more attention lock in the site but yet financial simple work.

Our files (attached) will let you know what we have so far. We need a complete change but the colours should be the same, however you can change them not running away to far from the original, and of course matching with the logo.

We need examples for 3 kind of layouts.

- A HOME welcome layout
- An internal Layout with sidebar
- And internal Layout wide

We can buy image licenses if needed for assets.
Actually there are 5 slide images placed on the Welcome HOME, we need those there, but you can improve with better images to match the new website!!!

Target Market(s)

Clients looking for financial advisers, tax and funds specialist, currency advisers

Industry/Entity Type

Financial

Requirements
Must have
• all the fonts must be in accordance with the financial market sites........the welcome home page must be precise, neat and information accurate........the menu should be elegant........main focus on the Home page, should be also the PRIVATE ACCESS box log in.......

```html
<!DOCTYPE html>
<html lang="en">
<head>
<meta charset="utf-8">
<title>Marlowe Capital Group</title>
<link href="https://fonts.googleapis.com/css2?family=Marcellus+SC&family=Arimo:wght@400;700&family=Ubuntu:wght@400;500&display=swap" rel="stylesheet">
<style>
:root{
  --orange:#e8661b;
  --orange-dark:#c9520f;
  --ink:#2a2a2a;
  --bar:#272624;
  --paper:#f2efe8;
  --text:#444;
  --muted:#7a7a7a;
  --blue:#1d6fb8;
  --red:#d0201e;
  --green:#2f8f2a;
  --line:#dcd8cf;
}
*{margin:0;padding:0;box-sizing:border-box}
html,body{width:768px;height:1200px;overflow:hidden}
body{background:var(--paper);font-family:"Arimo",Arial,sans-serif;color:var(--text);position:relative}
.abs{position:absolute}
.topbar{left:0;top:0;width:768px;height:34px;background:var(--bar)}
.btn-pill{top:7px;height:20px;border-radius:10px;background:var(--orange);border:1px solid #f0a36a;color:#fff;font-family:"Marcellus SC",serif;font-size:10px;line-height:18px;text-align:center;box-shadow:0 0 0 2px #3a3835}
.logo-box{left:84px;top:0;width:144px;height:77px;background:#f5f3ee;box-shadow:0 2px 4px rgba(0,0,0,.15);text-align:center}
.logo-mark{display:block;margin:12px auto 0;width:28px;height:28px;border-radius:50%;background:var(--orange)}
.logo-name{font-family:"Marcellus SC",serif;font-size:11px;color:var(--ink);margin-top:6px;letter-spacing:.3px}
.nav{left:272px;top:47px;width:414px;display:flex;justify-content:space-between;font-family:"Marcellus SC",serif;font-size:10px;color:#555;letter-spacing:.6px}
.nav .active{color:var(--orange)}
.nav-rule{left:272px;top:66px;width:414px;height:1px;background:var(--line)}
.nav-mark{left:272px;top:64px;width:39px;height:3px;background:var(--orange)}
.ticker{left:84px;top:109px;width:601px;height:12px;display:flex;gap:14px;overflow:hidden;font-size:6.4px;font-weight:700;white-space:nowrap}
.ticker .k{color:var(--blue)}.ticker .dn{color:var(--red)}.ticker .up{color:var(--green)}
.slider{left:84px;top:143px;width:601px;height:231px;background:linear-gradient(180deg,#8a8784 0%,#b9b6b3 45%,#6f6c69 100%);box-shadow:0 6px 8px -4px rgba(0,0,0,.3)}
.caption{left:0;top:149px;width:601px;height:82px;background:rgba(30,30,30,.72)}
.caption h2{position:absolute;left:81px;top:7px;font-family:"Ubuntu",sans-serif;font-weight:400;font-size:21px;color:#fff}
.caption p{position:absolute;left:82px;top:38px;width:450px;font-family:"Ubuntu",sans-serif;font-size:10px;line-height:14px;color:#eee}
.caption p b{font-weight:400;font-size:13px}
.arrow{width:19px;height:19px;border:1.5px solid #fff;border-radius:50%;top:182px}
.welcome h1{position:absolute;left:84px;top:421px;font-family:"Marcellus SC",serif;font-weight:400;font-size:16px;color:var(--ink);letter-spacing:.5px}
.welcome h1 span{color:var(--orange)}
.lead{left:84px;top:445px;width:400px;font-size:9.3px;line-height:12px;color:#222}
.body{left:84px;top:476px;width:400px;font-size:7.6px;line-height:11.4px;color:var(--muted)}
.access{left:531px;top:417px;width:155px;height:132px;background:var(--orange)}
.access-head{height:25px;background:var(--bar);color:#fff;font-family:"Marcellus SC",serif;font-size:11px;line-height:25px;padding-left:15px}
.field{position:absolute;left:18px;width:122px;height:17px;background:#fdf3e8;border:1px solid #d9864a;font-size:6.5px;color:#888;line-height:15px;padding-left:7px}
.forgot{position:absolute;left:16px;top:79px;font-size:5.8px;color:#4a2208}
.login{position:absolute;left:17px;top:100px;width:124px;height:20px;background:#242322;color:#fff;font-family:"Ubuntu",sans-serif;font-size:9px;text-align:center;line-height:20px}
.card{top:582px;width:187px;height:223px;background:#fff;border:1px solid #e5e1d8}
.card h3{position:absolute;left:13px;top:12px;font-family:"Marcellus SC",serif;font-weight:400;font-size:10.5px;color:var(--ink);letter-spacing:.4px;display:flex;align-items:center;gap:5px}
.card h3 i{width:8px;height:7px;background:var(--orange);display:inline-block;border-radius:2px}
.card .img{position:absolute;left:10px;top:29px;width:167px;height:99px}
.card p{position:absolute;left:12px;top:142px;width:163px;font-size:7.1px;line-height:11.4px;color:var(--muted)}
.card .more{position:absolute;right:19px;top:193px;width:62px;height:14px;background:var(--orange);color:#fff;font-size:6.6px;line-height:14px;text-align:center}
.verified-tab{left:289px;top:838px;width:190px;height:28px;border:1px solid var(--line);border-bottom:none;background:var(--paper);text-align:center;font-family:"Marcellus SC",serif;font-size:10.5px;line-height:28px;color:var(--ink);letter-spacing:.5px}
.badges{left:84px;top:866px;width:601px;height:52px;border:1px solid var(--line);display:flex;align-items:center;justify-content:space-around;padding:0 10px}
.badge{background:#c9c4ba}
.footer{left:84px;top:939px;width:601px;height:237px;background:var(--bar)}
.fcol{position:absolute;top:18px}
.fcol h4{font-family:"Marcellus SC",serif;font-weight:400;font-size:10.5px;color:var(--orange);letter-spacing:.6px;margin-bottom:4px}
.fcol li{list-style:none;font-size:6.6px;line-height:12.6px;color:#aaa}
.fcol li::before{content:"• ";color:#777}
.fsep{position:absolute;top:18px;width:1px;height:153px;background:#353432}
.legal{position:absolute;left:20px;top:188px;width:561px;font-size:6.2px;line-height:9px;color:#9a9a9a;text-align:center}
.copy{left:87px;top:1183px;font-size:6.4px;color:#444}
.disclaimer{right:86px;top:1183px;font-size:6.4px;color:#444}
</style>
</head>
<body>
<div class="abs topbar"></div>
<div class="abs btn-pill" style="left:541px;width:67px">Apply Now</div>
<div class="abs btn-pill" style="left:617px;width:69px">Contact Us</div>

<div class="abs logo-box">
  <span class="logo-mark"></span>
  <div class="logo-name">Marlowe Capital</div>
</div>

<nav class="abs nav">
  <span class="active">Home</span><span>About Us</span><span>Investments</span><span>Funds</span><span>Brokerage</span><span>Exchange</span><span>Accounts</span>
</nav>
<div class="abs nav-rule"></div>
<div class="abs nav-mark"></div>

<div class="abs ticker">
  <span><span class="k">GBP/AED = </span><span class="dn">5.72388 ▼</span></span>
  <span><span class="k">GBP/NOK = </span><span class="up">9.48889 ▲</span></span>
  <span><span class="k">GBP/SEK = </span><span class="up">10.35485 ▲</span></span>
  <span><span class="k">GBP/CHF = </span><span class="up">1.46663 ▲</span></span>
  <span><span class="k">GBP/JPY = </span><span class="dn">155.85433 ▼</span></span>
  <span><span class="k">GBP/HKD = </span><span class="dn">12.09626 ▼</span></span>
  <span><span class="k">GBP/CHF = </span><span class="up">1.46663 ▲</span></span>
  <span><span class="k">GBP/JPY</span></span>
</div>

<section class="abs slider" role="img" aria-label="Private jet parked on a wet runway, black and white photograph">
  <div class="abs caption">
    <h2>Find your own solution</h2>
    <p>Find the way of saving and investing that <b>suits you best.</b> We will help you understand your situation and your potential</p>
  </div>
  <svg class="abs arrow" style="left:10px" viewBox="0 0 19 19"><path d="M11 5 L7 9.5 L11 14" stroke="#fff" stroke-width="1.6" fill="none"/></svg>
  <svg class="abs arrow" style="left:572px" viewBox="0 0 19 19"><path d="M8 5 L12 9.5 L8 14" stroke="#fff" stroke-width="1.6" fill="none"/></svg>
</section>

<section class="welcome">
  <h1>Welcome to the <span>Marlowe Capital Group</span></h1>
  <p class="abs lead">Tempus proident, euismod ea class nisi, laborum harum distinctio. Quod? Inventore! Explicabo? Fames eaque felis, explicabo. Netus eos?</p>
  <p class="abs body">Occaecati. Dis reiciendis? Cupidatat ullamcorper? Ex. Natus mi incididunt! Porro mattis ducimus, dignissimos? Eget gravida, nec, aenean? Possimus incididunt mollit, est, proident cursus posuere minima nihil! Asperiores! Diamlorem cum platea neque dolores dolorum, nulla sodales iaculis veritatis, quis, nesciunt enim veniam vulputate, harum blanditiis vivamus! Hymenaeos pariatur vitae, inventore veritatis. Et voluptatem, accusantium, habitasse animi facere maxime fermentum cupiditate! Penatibus suspendisse varius ac, dolorum, proident etiam.</p>
</section>

<aside class="abs access">
  <div class="access-head">
    <svg width="8" height="9" viewBox="0 0 8 9" style="vertical-align:-1px"><rect x="0" y="4" width="8" height="5" fill="#fff"/><path d="M2 4V2.5a2 2 0 0 1 4 0V4" stroke="#fff" stroke-width="1.2" fill="none"/></svg>
    Private Access
  </div>
  <div class="field" style="top:34px">Acc. Number</div>
  <div class="field" style="top:56px">Acc. Password</div>
  <div class="forgot">Forgot acc number/password?</div>
  <div class="login">LOGIN</div>
</aside>

<article class="abs card" style="left:84px">
  <h3><i></i>Management &amp; Strategy</h3>
  <div class="img" role="img" aria-label="Hand writing on a printed bar chart beside a calculator" style="background:linear-gradient(135deg,#f4f4f2,#d9dde0 60%,#9ccf3a)"></div>
  <p>Doloribus tellus aptent nec dignissimos modi lobortis sapien consectetuer tempor dolores distinctio taciti nisl porta, molestie est scelerisque minima anim morbi...</p>
  <div class="more">Read More →</div>
</article>
<article class="abs card" style="left:290px">
  <h3><i></i>Funds</h3>
  <div class="img" role="img" aria-label="Blue world map overlaid with market figures" style="background:linear-gradient(135deg,#6fb2ea,#2a78c8 60%,#1a5aa8)"></div>
  <p>Doloribus tellus aptent nec dignissimos modi lobortis sapien consectetuer tempor dolores distinctio taciti nisl porta, molestie est scelerisque minima anim morbi...</p>
  <div class="more">Read More →</div>
</article>
<article class="abs card" style="left:497px">
  <h3><i></i>Currency Exchange</h3>
  <div class="img" role="img" aria-label="Green buy key and red sell key on a keyboard" style="background:linear-gradient(90deg,#2f9a2a 0%,#2f9a2a 48%,#c41e1e 52%,#c41e1e 100%)"></div>
  <p>Doloribus tellus aptent nec dignissimos modi lobortis sapien consectetuer tempor dolores distinctio taciti nisl porta, molestie est scelerisque minima anim morbi...</p>
  <div class="more">Read More →</div>
</article>

<div class="abs verified-tab">Verified and Protected By</div>
<div class="abs badges">
  <span class="badge" style="width:28px;height:22px;border-radius:50%"></span>
  <span class="badge" style="width:34px;height:18px"></span>
  <span class="badge" style="width:46px;height:18px"></span>
  <span class="badge" style="width:46px;height:18px"></span>
  <span class="badge" style="width:72px;height:18px"></span>
  <span class="badge" style="width:20px;height:22px"></span>
  <span class="badge" style="width:56px;height:18px"></span>
  <span class="badge" style="width:26px;height:26px;border-radius:50%"></span>
</div>

<footer class="abs footer">
  <div class="fcol" style="left:24px"><h4>About Us</h4><ul><li>History</li><li>expertize</li><li>Identity</li><li>Strategy</li><li>Contact us</li></ul></div>
  <div class="fsep" style="left:88px"></div>
  <div class="fcol" style="left:106px"><h4>Investments</h4><ul><li>Term Deposits</li><li>Managment &amp; Strategy</li><li>Client Relations</li><li>Financial Privacy</li><li>Tax Advice</li><li>Wealth Analysis &amp; Financial Planning</li><li>Active Advisory Group</li><li>Manager Selection Services</li><li>Private Equity</li></ul></div>
  <div class="fsep" style="left:246px"></div>
  <div class="fcol" style="left:264px"><h4>Funds</h4><ul><li>Overview</li><li>Administration</li><li>Funds Security</li><li>Core Services</li><li>Reporting</li><li>Revenue Oportunities</li><li>How it works?</li><li>Glossary</li></ul></div>
  <div class="fsep" style="left:356px"></div>
  <div class="fcol" style="left:376px"><h4>Currency Exchange</h4><ul><li>Foreign Exchange</li><li>Fx Forward</li><li>Fx Options</li></ul>
    <h4 style="margin-top:24px">Accounts</h4><ul><li>Apply Now</li><li>Private Access</li></ul></div>
  <div class="fsep" style="left:490px"></div>
  <div class="fcol" style="left:508px"><h4>Brokerage</h4><ul><li>Institutional</li><li>Research</li><li>Trading</li></ul></div>
  <p class="legal">By accessing the website of this group you agree that all content is provided for general information only and does not form investment advice. Rates shown are indicative and may change without notice. Past performance is no guide to future returns. Please read our terms carefully before you invest.</p>
</footer>

<div class="abs copy">© copyrights 2009 - 2013</div>
<div class="abs disclaimer">Legal Disclaimer</div>
</body>
</html>
```